Design our letter, business card, powerpoint and more

We have a logo and want a design for our business use. Letters (word template), business card (for printing) powerpoint presentation (template) and more.

```html
<!DOCTYPE html>
<html lang="en">
<head>
<meta charset="utf-8">
<title>NORDVERK – Presentation Template</title>
<link rel="stylesheet" href="https://fonts.googleapis.com/css2?family=Maven+Pro:wght@400;500;700&family=Open+Sans:wght@400;600&display=swap">
<style>
  :root {
    --stage: #2d2d2d;
    --white: #ffffff;
    --tint: #eaf2fd;
    --blue: #5aa8ea;
    --blue-light: #7bbcf0;
    --ink: #2e3238;
    --body: #7b8088;
    --logo-grey: #8a9098;
    --map-a: #e7e4df;
    --map-b: #d9d4ca;
  }
  * { box-sizing: border-box; margin: 0; padding: 0; }
  html, body { width: 1200px; height: 675px; overflow: hidden; }
  body { background: var(--stage); position: relative; font-family: "Open Sans", sans-serif; }

  .slide {
    position: absolute; width: 361px; height: 203px; border-radius: 19px;
    overflow: hidden; background: var(--white);
  }
  .slide--intro { left: 228px; top: 103px; }
  .slide--features { left: 611px; top: 103px; background: var(--tint); }
  .slide--contact { left: 228px; top: 349px; }
  .slide--closing { left: 611px; top: 349px; background: var(--tint); }

  .heading { font-family: "Maven Pro", sans-serif; font-weight: 500; color: var(--ink); position: absolute; white-space: nowrap; }
  .copy { position: absolute; font-size: 4.4px; line-height: 7px; color: var(--body); }
  .divider { position: absolute; }

  /* intro */
  .intro__halo { position: absolute; left: 140px; top: -18px; width: 238px; height: 238px; border-radius: 50%; background: var(--tint); }
  .intro__ring { position: absolute; left: 179px; top: 21px; width: 160px; height: 160px; border-radius: 50%; background: var(--white); }
  .intro__photo { position: absolute; left: 193px; top: 35px; width: 132px; height: 132px; border-radius: 50%;
    background: radial-gradient(circle at 35% 40%, #c9b7a4, #8a6a4e 55%, #4a3326); }
  .intro__badge { position: absolute; left: 223px; top: 65px; width: 72px; height: 72px; border-radius: 50%; background: var(--blue);
    display: flex; align-items: center; justify-content: center; }

  /* features */
  .feature { position: absolute; top: 0; width: 100px; height: 203px; }
  .feature__disc { position: absolute; left: 21px; top: 37px; width: 65px; height: 65px; border-radius: 50%; background: var(--white); }
  .feature__icon { position: absolute; left: 42px; top: 56px; }
  .feature .heading { left: 42px; top: 80px; font-size: 11.5px; }
  .feature .copy { left: 43px; top: 98px; width: 68px; }

  /* contact */
  .contact__map { position: absolute; left: -122px; top: 196px; width: 302px; height: 302px; border-radius: 50%;
    transform: translateY(-50%); margin-top: 0;
    background: linear-gradient(135deg, var(--map-b), var(--map-a) 55%, #ecebe8); }
  .contact__line { position: absolute; left: 219px; top: 144px; font-size: 4.4px; line-height: 7px; color: var(--body); }
  .contact__line a { color: var(--blue); }
  .contact__pin { position: absolute; left: 206px; top: 147px; }

  /* closing */
  .closing__disc { position: absolute; left: 20px; top: 15px; width: 172px; height: 172px; border-radius: 50%;
    background: linear-gradient(160deg, var(--blue-light), var(--blue)); }
  .closing__title { position: absolute; left: 20px; top: 77px; width: 172px; text-align: center;
    font-family: "Maven Pro", sans-serif; font-weight: 700; font-size: 22px; color: var(--white); }
  .closing__note { position: absolute; left: 20px; top: 116px; width: 172px; text-align: center; font-size: 3px; color: #e5f1fc; }
  .closing__arrow { position: absolute; left: 101px; top: 133px; }
  .closing__link { position: absolute; left: 77px; top: 156px; width: 58px; height: 11px; background: var(--white);
    font-size: 4px; line-height: 11px; text-align: center; color: var(--blue); }
  .closing__link u { color: var(--blue-light); }
  .closing__panel { position: absolute; left: 220px; top: 15px; width: 160px; height: 172px; border-radius: 86px 0 0 86px; background: var(--white); }
  .brand { position: absolute; left: 240px; top: 98px; width: 120px; text-align: center;
    font-family: "Maven Pro", sans-serif; font-weight: 500; font-size: 12px; color: var(--logo-grey); letter-spacing: 0.3px; }
</style>
</head>
<body>

<section class="slide slide--intro">
  <div class="intro__halo"></div>
  <div class="intro__ring"></div>
  <div class="intro__photo" role="img" aria-label="Photo of colleagues smiling around a table"></div>
  <div class="intro__badge">
    <svg width="22" height="20" viewBox="0 0 22 20"><path fill="#fff" d="M1 8h4v11H1zM7 8l5-7c1.6-.4 2.6.8 2.2 2.4L13 7h6c1.3 0 2.2 1.2 1.9 2.4l-2 8c-.3 1-1.1 1.6-2.1 1.6H7z"/></svg>
  </div>
  <h2 class="heading" style="left:36px;top:31px;font-size:15px;">Title text slide</h2>
  <svg class="divider" style="left:36px;top:58px" width="24" height="8" viewBox="0 0 24 8"><circle cx="2.5" cy="4" r="2.2" fill="#5aa8ea"/><circle cx="11" cy="4" r="3.8" fill="#5aa8ea"/><line x1="11" y1="4" x2="20" y2="4" stroke="#5aa8ea" stroke-width="1"/><circle cx="20.5" cy="4" r="2" fill="#5aa8ea"/></svg>
  <p class="copy" style="left:36px;top:77px;width:132px;">Ut enim ad minim veniam, quis nostrud exercitation ullamco laboris nisi ut aliquip ex ea commodo consequat. Duis aute irure dolor in reprehenderit in voluptate velit esse cillum dolore eu fugiat nulla pariatur. Excepteur sint occaecat cupidatat non proident, sunt in culpa qui officia deserunt mollit anim id est laborum. Sed ut perspiciatis unde omnis iste natus error sit voluptatem accusantium doloremque laudantium, totam rem aperiam.</p>
</section>

<section class="slide slide--features">
  <div class="feature" style="left:0">
    <div class="feature__disc"></div>
    <svg class="feature__icon" width="17" height="15" viewBox="0 0 17 15"><rect width="17" height="15" rx="1.5" fill="#5aa8ea"/><path d="M2 12l4-5 3 3 2-2 4 4z" fill="#fff"/><circle cx="12" cy="4.5" r="1.5" fill="#fff"/></svg>
    <h3 class="heading">Subtitle text</h3>
    <p class="copy">Lorem ipsum sed dolor sit sed amet, consectetur adipiscing incididunt ut labore et dolore minim veniam, laboris quis nostrud exercitation ullamco dolor in reprehenderit in dolor ipsum dolor sit amet, consectetur eiusmod tempor incididunt</p>
  </div>
  <div class="feature" style="left:105px">
    <div class="feature__disc"></div>
    <svg class="feature__icon" width="19" height="16" viewBox="0 0 19 16"><path d="M0 6L9.5 0 19 6v10H0z" fill="#5aa8ea"/><path d="M0 6l9.5 6L19 6" fill="none" stroke="#fff" stroke-width="1.3"/></svg>
    <h3 class="heading">Subtitle text</h3>
    <p class="copy">Lorem ipsum sed dolor sit sed amet, consectetur adipiscing incididunt ut labore et dolore minim veniam, laboris quis nostrud exercitation ullamco dolor in reprehenderit in dolor ipsum dolor sit amet, consectetur eiusmod tempor incididunt</p>
  </div>
  <div class="feature" style="left:210px">
    <div class="feature__disc"></div>
    <svg class="feature__icon" width="14" height="18" viewBox="0 0 14 18"><path d="M0 1.5A1.5 1.5 0 011.5 0H9l5 5v11.5a1.5 1.5 0 01-1.5 1.5h-11A1.5 1.5 0 010 16.5z" fill="#5aa8ea"/><path d="M9 0v5h5" fill="#cfe4f8"/></svg>
    <h3 class="heading">Subtitle text</h3>
    <p class="copy">Lorem ipsum sed dolor sit sed amet, consectetur adipiscing incididunt ut labore et dolore minim veniam, laboris quis nostrud exercitation ullamco dolor in reprehenderit in dolor ipsum dolor sit amet, consectetur eiusmod tempor incididunt</p>
  </div>
</section>

<section class="slide slide--contact">
  <div class="contact__map" role="img" aria-label="Street map showing the office location" style="top:196px;"></div>
  <h2 class="heading" style="left:206px;top:45px;font-size:15px;">Contact us</h2>
  <svg class="divider" style="left:206px;top:71px" width="24" height="8" viewBox="0 0 24 8"><circle cx="2.5" cy="4" r="2.2" fill="#5aa8ea"/><circle cx="11" cy="4" r="3.8" fill="#5aa8ea"/><line x1="11" y1="4" x2="20" y2="4" stroke="#5aa8ea" stroke-width="1"/><circle cx="20.5" cy="4" r="2" fill="#5aa8ea"/></svg>
  <p class="copy" style="left:206px;top:89px;width:115px;">Lorem ipsum sed dolor sit sed amet, consectetur adipiscing elit, sed do eiusmod tempor incididunt ut labore et dolore magna aliqua. Ut proident ad minim veniam, laboris quis proident nostrud exercitation ullamco laboris nisi ut aliquip ex ea commodo ut consequat. Duis aute irure dolor in</p>
  <svg class="contact__pin" width="9" height="9" viewBox="0 0 9 9"><circle cx="4.5" cy="4.5" r="4.5" fill="#5aa8ea"/><path d="M4.5 2.7a1.3 1.3 0 110 2.6 1.3 1.3 0 010-2.6zM4.5 7L3 5.3h3z" fill="#fff"/></svg>
  <p class="contact__line">2041 Elmwood Lane, Riverton, CA, USA<br>+15550142, <a>hello@studioname.com</a></p>
</section>

<section class="slide slide--closing">
  <div class="closing__disc"></div>
  <h2 class="closing__title">Thank you!</h2>
  <p class="closing__note">Some text can be here</p>
  <svg class="closing__arrow" width="9" height="9" viewBox="0 0 9 9"><path d="M4.5 0v8M1 4.8l3.5 3.5L8 4.8" fill="none" stroke="#fff" stroke-width="1"/></svg>
  <div class="closing__link">LINK! <u>NORDVERK</u></div>
  <div class="closing__panel"></div>
  <div class="brand">NORDVERK</div>
</section>

</body>
</html>
```